Construction company Needs a Presentation Folder Design

Construction/Restoration company based in Chicago needs a Presentation Folder for our customers. Folder must have 2 inside pockets with one having a cut for the business card. We focus on residential projects helping our customers to replace roofs, siding, gutters and more... . 80% of our business is HAIL & WIND RESTORATION helping homeowners to navigate through home restoration process when insurance companies gets involved after storms. Final design should communicate professionalism and trust. Our moto is "Trust The Professionals"
Target Market(s)
Chicago local market
Industry/Entity Type
Residential Construction
Font styles to use
Other font styles liked:
- Avenir
Requirements
Must have
- Please incorporate a picture of the storm, since we are Wind and hail restoration contractor
- Services:
- Wind/Hail restoration;
- Roofing;
- Siding;
- Gutters;

Nice to have
- Clean design, Front and Back
- Icons (where applicable)

Should not have
- Should not follow our logo roof line design.
- Don't make a design to simple either, please

```html
<!DOCTYPE html>
<html lang="en">
<head>
<meta charset="utf-8">
<title>Harbor Ridge Exteriors – Presentation Folder</title>
<link href="https://fonts.googleapis.com/css2?family=Montserrat:ital,wght@0,400;0,500;0,700;0,800;1,400;1,700&display=swap" rel="stylesheet">
<style>
  :root {
    --page: #ffffff;
    --charcoal: #484442;
    --charcoal-deep: #3f3b39;
    --red: #e2141c;
    --red-soft: #ea2229;
    --white: #ffffff;
    --fold: #d4237d;
  }
  html, body {
    margin: 0;
    padding: 0;
    width: 848px;
    height: 1200px;
    overflow: hidden;
    background: var(--page);
  }
  .folder-dieline {
    position: absolute;
    left: 44px;
    top: 260px;
    width: 760px;
    height: 680px;
    font-family: "Montserrat", sans-serif;
  }
  .panel { fill: var(--charcoal); }
  .pocket { fill: var(--charcoal); stroke: var(--fold); stroke-width: 1; }
  .fold-line { stroke: var(--fold); stroke-width: 0.8; stroke-dasharray: 3 3; }
  .trim-line { fill: none; stroke: var(--fold); stroke-width: 0.8; }
  .accent-red { fill: var(--red); }
  .accent-red-soft { fill: var(--red-soft); }
  .crease { stroke: #8a2a1c; stroke-width: 2; }
  .card-slit { stroke: var(--red); stroke-width: 1; }
  .brand-name { fill: var(--red); font-weight: 800; font-size: 29px; letter-spacing: 0.5px; }
  .brand-sub { fill: var(--white); font-weight: 500; font-size: 16px; letter-spacing: 1.6px; }
  .services-title { font-weight: 700; font-size: 14px; fill: var(--white); }
  .services-title .highlight { fill: var(--red); }
  .service-item { fill: var(--white); font-size: 10.5px; font-weight: 400; }
  .service-more { fill: var(--white); font-size: 14px; font-style: italic; }
  .service-more .strong { font-weight: 700; }
  .icon-stroke { fill: none; stroke: var(--red); stroke-width: 1.6; }
  .motto-top { fill: none; stroke: var(--red); stroke-width: 0.7; font-size: 17px; font-style: italic; }
  .motto-main { fill: var(--white); font-weight: 700; font-size: 17px; letter-spacing: 0.3px; }
</style>
</head>
<body>
<svg class="folder-dieline" viewBox="135 750 790 707" xmlns="http://www.w3.org/2000/svg">
  <defs>
    <linearGradient id="storm-photo-tone" x1="0" y1="0" x2="1" y2="1">
      <stop offset="0" stop-color="#a6b39a"/>
      <stop offset="0.45" stop-color="#c9c7bb"/>
      <stop offset="0.75" stop-color="#6e7d55"/>
      <stop offset="1" stop-color="#9a9a92"/>
    </linearGradient>
  </defs>

  <!-- Cover spread -->
  <rect class="panel back-cover" x="135" y="750" width="393" height="530"/>
  <rect class="panel front-cover" x="528" y="750" width="397" height="530"/>

  <!-- Red angular bands -->
  <polygon class="accent-red" points="135,1160 245,1215 360,1280 135,1280"/>
  <polygon class="accent-red-soft" points="245,1215 752,930 530,1280 360,1280"/>
  <line class="crease" x1="245" y1="1215" x2="360" y2="1280"/>

  <!-- Storm damage photograph area -->
  <polygon role="img" aria-label="Photo of a fallen tree lying against a two-storey house after a storm"
           points="752,930 925,1180 925,1270 605,1168" fill="url(#storm-photo-tone)"/>

  <!-- Fold line -->
  <line class="fold-line" x1="528" y1="750" x2="528" y2="1280"/>

  <!-- Front cover brand -->
  <g class="brand">
    <text class="brand-name" x="822" y="872" text-anchor="end">HARBOR RIDGE</text>
    <text class="brand-sub" x="822" y="892" text-anchor="end">EXTERIORS INC.</text>
  </g>

  <!-- Motto -->
  <text class="motto-top" x="588" y="1239">TRUST THE</text>
  <text class="motto-main" x="588" y="1256">PROFESSIONALS</text>

  <!-- Back cover services -->
  <g class="services">
    <rect class="accent-red" x="158" y="946" width="38" height="38"/>
    <rect class="accent-red" x="157" y="996" width="3" height="20"/>
    <text class="services-title" x="165" y="1011">Our <tspan class="highlight">Services</tspan></text>

    <path class="icon-stroke" d="M170 1054 V1043 L179 1035 L188 1043 V1054 Z"/>
    <text class="service-item" x="199" y="1051">Roofing</text>

    <g class="icon-stroke">
      <rect x="168" y="1071" width="22" height="15"/>
      <line x1="168" y1="1076" x2="190" y2="1076"/>
      <line x1="168" y1="1081" x2="190" y2="1081"/>
    </g>
    <text class="service-item" x="199" y="1083">Siding</text>

    <path class="icon-stroke" d="M173 1121 V1106 H188"/>
    <text class="service-item" x="199" y="1117">Gutters</text>

    <text class="service-more" x="166" y="1143">And <tspan class="strong">More.....</tspan></text>
  </g>

  <!-- Inside pockets -->
  <polygon class="pocket" points="135,1282 525,1282 507,1457 135,1457"/>
  <polygon class="pocket" points="532,1282 925,1282 925,1457 550,1457"/>
  <line class="card-slit" x1="640" y1="1348" x2="668" y2="1322"/>
  <line class="card-slit" x1="786" y1="1418" x2="814" y2="1392"/>

  <rect class="trim-line" x="135" y="750" width="790" height="530"/>
</svg>
</body>
</html>
```